The Brightwater Compass Business Card

We need an attractive business card with the logo that we bought from ArtVantly last year.
Our mission is to contribute to change the way today's leaders manage business companies bringing value to the workplace and helping them to build a new model of creating wealth.
Our logo is clear about our values : we seek Positive Change through People and are convinced that the pursuit of individual well-being and the chase of economic results can converge with the right management.
Management Consulting
Corinne Fabrelle
+34 612 98 70 31
corinne.fabrelle@thebrightwatercompass-mail.net
www.thebrightwatercompass-mail.net

```html
<!DOCTYPE html>
<html lang="en">
<head>
<meta charset="utf-8">
<title>The Brightwater Compass Business Card</title>
<link href="https://fonts.googleapis.com/css2?family=Open+Sans:wght@400;600;700&display=swap" rel="stylesheet">
<style>
  :root {
    --backdrop: #e8e9eb;
    --teal: #089d99;
    --teal-deep: #07918d;
    --teal-ink: #16807e;
    --paper: #ffffff;
    --white: #ffffff;
  }
  html, body {
    margin: 0;
    padding: 0;
    width: 1200px;
    height: 720px;
    overflow: hidden;
    background: var(--backdrop);
    font-family: "Open Sans", Arial, sans-serif;
  }
  .stage {
    position: relative;
    width: 1200px;
    height: 720px;
  }
  .card {
    position: absolute;
    top: 241px;
    width: 420px;
    height: 240px;
    box-sizing: border-box;
    text-align: center;
  }
  .card--front {
    left: 147px;
    background: linear-gradient(135deg, var(--teal-deep) 0%, var(--teal) 60%, #0aa5a1 100%);
    color: var(--white);
  }
  .card--back {
    left: 633px;
    background: var(--paper);
    color: var(--teal-ink);
  }
  .brand {
    display: flex;
    flex-direction: column;
    align-items: center;
  }
  .brand__mark {
    border-radius: 50%;
    background: currentColor;
  }
  .brand__name {
    font-weight: 600;
    letter-spacing: 0.02em;
    white-space: nowrap;
  }
  .card--front .brand {
    margin-top: 68px;
  }
  .card--front .brand__mark {
    width: 44px;
    height: 44px;
  }
  .card--front .brand__name {
    margin-top: 14px;
    font-size: 19px;
  }
  .card--front .website {
    position: absolute;
    left: 0;
    right: 0;
    top: 199px;
    font-size: 10px;
    font-weight: 400;
  }
  .card--back .brand {
    margin-top: 25px;
  }
  .card--back .brand__mark {
    width: 26px;
    height: 26px;
  }
  .card--back .brand__name {
    margin-top: 7px;
    font-size: 12px;
  }
  .person {
    margin-top: 20px;
  }
  .person__name {
    font-size: 11.5px;
    font-weight: 700;
    letter-spacing: 0.1em;
    text-transform: uppercase;
  }
  .person__role {
    margin-top: 1px;
    font-size: 10.5px;
    font-weight: 400;
    letter-spacing: 0.16em;
    text-transform: uppercase;
  }
  .contact {
    margin-top: 21px;
    font-size: 10.5px;
    line-height: 14.5px;
    font-weight: 400;
  }
</style>
</head>
<body>
<main class="stage">
  <section class="card card--front" aria-label="Business card front">
    <div class="brand">
      <span class="brand__mark" aria-hidden="true"></span>
      <span class="brand__name">The Brightwater Compass</span>
    </div>
    <p class="website">www.thebrightwatercompass-mail.net</p>
  </section>

  <section class="card card--back" aria-label="Business card back">
    <div class="brand">
      <span class="brand__mark" aria-hidden="true"></span>
      <span class="brand__name">The Brightwater Compass</span>
    </div>
    <div class="person">
      <div class="person__name">Corinne Fabrelle</div>
      <div class="person__role">Life Coach</div>
    </div>
    <div class="contact">
      <div class="contact__phone">+34 612 98 70 31</div>
      <div class="contact__email">corinne.fabrelle@thebrightwatercompass-mail.net</div>
      <div class="contact__web">www.thebrightwatercompass-mail.net</div>
    </div>
  </section>
</main>
</body>
</html>
```